Criação de Papelaria Profissional para Crianças & Infantil
A empresa queria:
" Esta empresa preza por vender roupas de altíssima qualidade e marcas diferenciadas, a fim de encantar pais e filhos, garantindo conforto e estilo aos pequenos. "

```html
<!DOCTYPE html>
<html lang="pt-BR">
<head>
<meta charset="UTF-8">
<title>Assinatura de e-mail – Pimpolu</title>
<link href="https://fonts.googleapis.com/css2?family=Montserrat:wght@700&family=Nunito:wght@800&family=Arimo:wght@400&display=swap" rel="stylesheet">
<style>
  :root {
    --bg-dark: #cfd0d2;
    --bg-light: #dcdddf;
    --purple: #6e2b8f;
    --purple-title: #5b2a83;
    --white: #ffffff;
    --pink: #f08fb0;
    --yellow: #f6c46b;
    --blue: #7fc4e8;
    --green: #9fd8c4;
    --icon: #f3b6cf;
  }
  * { margin: 0; padding: 0; box-sizing: border-box; }
  html, body { width: 1200px; height: 1200px; overflow: hidden; }
  body {
    background: linear-gradient(135deg, var(--bg-dark) 50%, var(--bg-light) 50%);
    position: relative;
    font-family: "Arimo", Arial, sans-serif;
  }
  .section-title {
    position: absolute;
    top: 50px; left: 0; width: 100%;
    text-align: center;
    font-family: "Montserrat", sans-serif;
    font-weight: 700;
    font-size: 32px;
    letter-spacing: 3px;
    color: var(--purple-title);
  }
  .signature {
    position: absolute;
    left: 125px; top: 420px;
    width: 948px; height: 353px;
    background: var(--white);
    border-radius: 0 0 0 56px;
    box-shadow: 0 2px 6px rgba(0,0,0,0.08);
  }
  .brand {
    position: absolute;
    left: 0; top: 0; width: 460px; height: 100%;
    display: flex; align-items: center; justify-content: center;
    font-family: "Nunito", sans-serif;
    font-weight: 800;
    font-size: 84px;
    color: var(--purple);
  }
  .stripes {
    position: absolute;
    left: 458px; top: 0; width: 40px; height: 100%;
    border-radius: 70px 0 0 0;
    overflow: hidden;
    display: flex; flex-direction: column;
  }
  .stripes span { flex: 1; }
  .stripes .s1 { background: var(--pink); }
  .stripes .s2 { background: var(--yellow); }
  .stripes .s3 { background: var(--blue); }
  .stripes .s4 { background: var(--green); }
  .contact-panel {
    position: absolute;
    left: 475px; top: 0; right: 0; height: 100%;
    background: var(--purple);
    border-radius: 70px 56px 0 0;
    color: var(--white);
    padding: 62px 0 0 42px;
    font-size: 27px;
    line-height: 1.1;
  }
  .contact-row {
    display: flex; align-items: flex-start; gap: 14px;
    margin-bottom: 22px;
  }
  .contact-row svg { flex: none; width: 26px; height: 26px; margin-top: 2px; }
  .contact-row p { margin: 0; }
</style>
</head>
<body>
  <h1 class="section-title">ASSINATURA</h1>

  <div class="signature">
    <div class="brand">Pimpolu</div>

    <div class="stripes">
      <span class="s1"></span><span class="s2"></span><span class="s3"></span><span class="s4"></span>
    </div>

    <div class="contact-panel">
      <div class="contact-row">
        <svg viewBox="0 0 24 24" fill="none" stroke="var(--icon)" stroke-width="2" stroke-linecap="round" stroke-linejoin="round"><path d="M6 3h3l2 5-2.5 1.5a11 11 0 0 0 6 6L16 13l5 2v3a2 2 0 0 1-2 2A16 16 0 0 1 4 5a2 2 0 0 1 2-2z"/></svg>
        <p>(99) 98200-5050<br>(99) 99300-6060</p>
      </div>
      <div class="contact-row">
        <svg viewBox="0 0 24 24" fill="none" stroke="var(--yellow)" stroke-width="2" stroke-linecap="round" stroke-linejoin="round"><path d="M12 22s7-7 7-12a7 7 0 0 0-14 0c0 5 7 12 7 12z"/><circle cx="12" cy="10" r="2.5"/></svg>
        <p>Rua das Flores, 310 - Centro<br>Cidade/UF - CEP: 34700-210</p>
      </div>
      <div class="contact-row">
        <svg viewBox="0 0 24 24" fill="none" stroke="var(--icon)" stroke-width="2" stroke-linejoin="round"><rect x="3" y="5" width="18" height="14" rx="2"/><path d="M3 7l9 6 9-6"/></svg>
        <p>pimpolu@mail.com</p>
      </div>
      <div class="contact-row">
        <svg viewBox="0 0 24 24" fill="none" stroke="var(--blue)" stroke-width="2"><circle cx="12" cy="12" r="8"/></svg>
        <p>@pimpolu</p>
      </div>
    </div>
  </div>
</body>
</html>
```